Branding for Clear Current Honours program collateral

The Clear Current Honours, hosted by the Flowline Sector Council, are an annual awards program to recognise excellence in the Australian water industry. The awards presentation ceremony is held over a formal luncheon, with a MC and Keynote Speaker. The awards event is a premium experience for business professionals that work in the work sector. It is a corporate business luncheon with management level professionals in attendance. We are seeking branding design elements that we can use on all awards collateral including the website, printed invitation, event program, social media posts etc. The Clear Current Honours are well known in the industry and recognised by its logo and corporate colours (attached). We would like these incorporated into the design.

Target Market(s)

business professionals

Industry/Entity Type

Water Company

Requirements
Must have
• event logo, corporate colours

```html
<!DOCTYPE html>
<html lang="en">
<head>
<meta charset="utf-8">
<title>Clear Current Honours – Branding</title>
<link href="https://fonts.googleapis.com/css2?family=Montserrat:wght@400;500;600&family=Raleway:wght@300&display=swap" rel="stylesheet">
<style>
  :root {
    --paper: #ffffff;
    --gold-light: #dbc963;
    --gold-mid: #c9b657;
    --gold-deep: #8f7f27;
    --water-blue: #6f8fd8;
    --water-teal: #3f9da8;
    --water-sky: #7fd6f2;
    --aqua: #4be8cc;
    --aqua-soft: #55eabf;
    --text-light: #ffffff;
  }
  html, body {
    margin: 0;
    padding: 0;
    overflow: hidden;
    background: var(--paper);
  }
  .canvas {
    position: relative;
    width: 1200px;
    height: 1200px;
    background: var(--paper);
    overflow: hidden;
    font-family: "Montserrat", sans-serif;
  }
  .event-banner {
    position: absolute;
    left: 299px;
    top: 174px;
    width: 603px;
    height: 250px;
    background: linear-gradient(90deg, var(--gold-light) 0%, var(--gold-light) 45%, var(--gold-mid) 65%, var(--gold-deep) 100%);
  }
  .banner-splash {
    position: absolute;
    right: 40px;
    top: 0;
    width: 150px;
    height: 250px;
    background: linear-gradient(90deg, rgba(63,157,168,0) 0%, var(--water-teal) 40%, var(--water-blue) 100%);
    opacity: 0.85;
  }
  .banner-splash-left {
    position: absolute;
    left: 30px;
    bottom: 0;
    width: 240px;
    height: 110px;
    background: radial-gradient(ellipse at 60% 100%, rgba(127,214,242,0.8) 0%, rgba(127,214,242,0) 70%);
  }
  .banner-frame {
    position: absolute;
    left: 0;
    top: 0;
    width: 603px;
    height: 250px;
  }
  .event-title {
    position: absolute;
    left: 0;
    width: 603px;
    top: 70px;
    margin: 0;
    text-align: center;
    color: var(--text-light);
    font-weight: 600;
    font-size: 33px;
    letter-spacing: 0.5px;
    text-shadow: 0 2px 4px rgba(0,0,0,0.25);
  }
  .event-subtitle {
    position: absolute;
    left: 0;
    width: 603px;
    top: 117px;
    text-align: center;
    color: var(--text-light);
    font-weight: 500;
    font-size: 12px;
    letter-spacing: 3px;
  }
  .event-region {
    position: absolute;
    left: 0;
    width: 603px;
    top: 142px;
    text-align: center;
    color: var(--text-light);
    font-weight: 400;
    font-size: 11px;
    letter-spacing: 2.5px;
  }
  .year-ring {
    position: absolute;
    left: 654px;
    top: 328px;
    width: 144px;
    height: 144px;
  }
  .year-label {
    position: absolute;
    left: 654px;
    top: 380px;
    width: 144px;
    text-align: center;
    color: var(--text-light);
    font-family: "Raleway", sans-serif;
    font-weight: 300;
    font-size: 25px;
    letter-spacing: 1px;
  }
  .splash-panel {
    position: absolute;
    left: 354px;
    top: 524px;
    width: 490px;
    height: 438px;
    background:
      radial-gradient(ellipse at 70% 45%, rgba(255,255,255,0.9) 0%, rgba(255,255,255,0.55) 22%, rgba(255,255,255,0) 45%),
      radial-gradient(ellipse at 55% 75%, rgba(40,120,200,0.35) 0%, rgba(40,120,200,0) 40%),
      var(--aqua);
  }
</style>
</head>
<body>
<div class="canvas">
  <section class="event-banner">
    <div class="banner-splash" role="img" aria-label="Blue water splash texture"></div>
    <div class="banner-splash-left" role="img" aria-label="Light blue water spray"></div>
    <svg class="banner-frame" viewBox="0 0 603 250" aria-hidden="true">
      <g fill="none" stroke="#ffffff" stroke-width="3">
        <polyline points="213,124 121,124 121,62 497,62 497,124 404,124"/>
      </g>
    </svg>
    <h1 class="event-title">Clear Current</h1>
    <div class="event-subtitle">HONOURS</div>
    <div class="event-region">SOUTH AUSTRALIA</div>
  </section>

  <svg class="year-ring" viewBox="0 0 144 144" aria-hidden="true">
    <defs>
      <linearGradient id="ringGold" x1="0" y1="0" x2="0" y2="1">
        <stop offset="0" stop-color="#d9c45c"/>
        <stop offset="1" stop-color="#9c8a2e"/>
      </linearGradient>
    </defs>
    <circle cx="72" cy="72" r="63" fill="none" stroke="url(#ringGold)" stroke-width="8"/>
  </svg>
  <div class="year-label">2019</div>

  <div class="splash-panel" role="img" aria-label="White and blue water splash on aqua background"></div>
</div>
</body>
</html>
```